Cutting Edge Cloud Hosting Provider needs business card design

We are a new Cloud Hosting Provider called Verdalo Hosting. (Verdalo means cloudy in Spanish.) We provide clients with virtual resources and not virtual machines directly. Our clients purchase the resources that they will use (RAM,CPU, Hard drive space) then use those resources in as many virtual machines as they like.

We are looking for a business card design that is cutting edge and hip.
Updates

The name of the company is "Verdalo Hosting". Please include the "Hosting" part of our name in the design.

Thanks

Target Market(s)

21-35 developers and I.T. Staff

Industry/Entity Type

Business

Requirements
Must have
• Rounded corners, Must Incorporate our logo, individual's name must be prominent

```html
<!DOCTYPE html>
<html lang="en">
<head>
<meta charset="utf-8">
<title>Verdalo Hosting – Business Card</title>
<link rel="stylesheet" href="https://fonts.googleapis.com/css2?family=Nunito+Sans:wght@400;700&display=swap">
<style>
  :root {
    --navy: #1b3766;
    --band-dark: #13305f;
    --band-light: #a6bedb;
    --sky-center: #b4e2f7;
    --sky-edge: #1ba1df;
    --divider: #8fb3dc;
    --paper: #ffffff;
    --stage-top: #ffffff;
    --stage-bottom: #d9d9d9;
  }
  * { box-sizing: border-box; margin: 0; padding: 0; }
  html, body { width: 1200px; height: 456px; overflow: hidden; }
  body {
    position: relative;
    background: linear-gradient(180deg, var(--stage-bottom) 0%, var(--stage-top) 22%, var(--stage-top) 78%, var(--stage-bottom) 100%);
    font-family: "Nunito Sans", sans-serif;
    color: var(--navy);
  }
  .card {
    position: absolute;
    top: 84px;
    width: 514px;
    height: 286px;
    border-radius: 30px;
    overflow: hidden;
    box-shadow: 0 1px 4px rgba(0,0,0,0.25);
  }
  .card--front {
    left: 73px;
    background: radial-gradient(ellipse 60% 70% at 50% 45%, var(--sky-center) 0%, var(--sky-edge) 100%);
  }
  .card--back { left: 614px; background: var(--paper); }

  .wordmark {
    position: absolute;
    text-align: center;
    font-weight: 700;
    color: var(--navy);
    line-height: 1;
  }
  .wordmark__name { display: block; letter-spacing: 0.5px; }
  .wordmark__sub { display: block; text-transform: uppercase; }
  .card--front .wordmark { left: 0; right: 0; top: 118px; }
  .card--front .wordmark__name { font-size: 56px; }
  .card--front .wordmark__sub { font-size: 15px; letter-spacing: 13px; margin-top: 6px; padding-left: 13px; }
  .tagline {
    position: absolute; left: 0; right: 0; top: 234px;
    text-align: center; font-size: 14.5px; color: var(--navy);
  }

  .card--back .wordmark { left: 20px; width: 210px; top: 128px; }
  .card--back .wordmark__name { font-size: 41px; }
  .card--back .wordmark__sub { font-size: 11px; letter-spacing: 10px; margin-top: 5px; padding-left: 10px; }
  .divider {
    position: absolute; left: 256px; top: 80px;
    width: 2px; height: 126px; background: var(--divider);
  }
  .contact { position: absolute; left: 277px; top: 95px; }
  .contact__name { font-size: 20px; font-weight: 700; line-height: 1.2; }
  .contact__line { font-size: 14.5px; line-height: 19px; }
  .bands { position: absolute; left: 0; bottom: 0; width: 514px; height: 24px; }
</style>
</head>
<body>
  <section class="card card--front">
    <div class="wordmark">
      <span class="wordmark__name">Verdalo</span>
      <span class="wordmark__sub">Hosting</span>
    </div>
    <p class="tagline">Cloud Hosting Provider</p>
  </section>

  <section class="card card--back">
    <div class="wordmark">
      <span class="wordmark__name">Verdalo</span>
      <span class="wordmark__sub">Hosting</span>
    </div>
    <div class="divider"></div>
    <div class="contact">
      <p class="contact__name">Delio Marsten</p>
      <p class="contact__line">Vice-President</p>
      <p class="contact__line">p. 555.014.3872</p>
      <p class="contact__line">c. 555.016.4490</p>
      <p class="contact__line">delio@verdalo.com</p>
    </div>
    <svg class="bands" viewBox="0 0 514 24" preserveAspectRatio="none" aria-hidden="true">
      <polygon points="0,0 254,0 236,24 0,24" fill="var(--band-light)"/>
      <polygon points="260,0 514,0 514,24 242,24" fill="var(--band-dark)"/>
    </svg>
  </section>
</body>
</html>
```